Wine Label for a Prosecco Wine Called Vuro

Prosecco is a white sparkling wine from Italy. We are looking for an eye catching, elegant label for this prosecco that is called "Vuro" because it is a young, fresh, lively white sparkling wine. (We do not want to see children or babies featured on the label-- just the name VURO please.) Attached is the old label for your reference, and the bottle type that will be used , which is a dark green Burgundy style bottle (pls ignore the label on the bottle). Please no grapes or wine glasses on the label. We are looking for something: eye catching / fun / ELEGANT (not cheap). We would be happy with a fun color too. Remember-- elegant, eye catching! Thanks!
Updates

Hi All, I think I made a mistake in my brief and have updated it. I also uploaded a competitor's label that we like very much to give better direction to what we are looking for. Also, the word Vuro cannot be vertical, nor can it be broken. It needs to read: VURO or Vuro. Thanks

Target Market(s)

American adults male and female.

Colors
abd036
33a6d7
33b8a4
ffcf3e

Requirements
Must have
• The mandatory information as shown on old labels. The word VURO should be very prominent.
Nice to have
• The uploaded photo of a competitor's prosecco shows a label we really like... if you could play around with this shape and style we'd be very happy.
Should not have
• No grape images, no wine glass images, no images of babies or children.

```html
<!DOCTYPE html>
<html lang="it">
<head>
<meta charset="utf-8">
<title>Vuro Prosecco – Label</title>
<link rel="stylesheet" href="https://fonts.googleapis.com/css2?family=Great+Vibes&family=Libre+Baskerville:ital,wght@1,400;1,700&family=Poiret+One&family=Tinos&display=swap">
<style>
  :root {
    --backdrop: #ececec;
    --label-black: #141414;
    --label-edge: #0a0a0a;
    --gold: #f0a81c;
    --gold-soft: #c98a14;
    --ink-white: #ffffff;
    --ink-grey: #e6e6e6;
  }
  * { margin: 0; padding: 0; box-sizing: border-box; }
  html, body {
    width: 1200px; height: 1000px; overflow: hidden;
    background: var(--backdrop);
  }
  .canvas { position: relative; width: 1200px; height: 1000px; }

  .label {
    position: absolute; left: 228px; top: 104px;
    width: 744px; height: 792px;
    filter: drop-shadow(6px 8px 10px rgba(0,0,0,0.35));
  }
  .label-shape { position: absolute; inset: 0; }

  .crest {
    position: absolute; left: 282px; top: 58px;
    width: 180px; height: 124px;
    background: radial-gradient(ellipse at center, #d9a52a 0%, #b7821a 45%, rgba(20,20,20,0) 72%);
  }
  .product-type {
    position: absolute; left: 0; width: 100%; top: 212px;
    text-align: center; color: var(--ink-white);
    font: italic 700 44px/1 "Libre Baskerville", serif;
  }
  .divider-ornament {
    position: absolute; left: 336px; top: 290px;
    width: 72px; height: 36px;
    background: radial-gradient(ellipse at center, var(--gold) 0%, var(--gold-soft) 50%, rgba(20,20,20,0) 75%);
  }
  .wine-name {
    position: absolute; left: 0; width: 100%; top: 364px;
    text-align: center; color: var(--ink-white);
    font: 400 200px/1 "Great Vibes", cursive;
    text-shadow: 0 6px 10px rgba(0,0,0,0.6);
  }
  .region {
    position: absolute; left: 0; width: 100%; top: 560px;
    text-align: center; color: var(--ink-white);
    font: italic 700 26px/1 "Libre Baskerville", serif;
    padding-left: 20px;
  }
  .appellation {
    position: absolute; left: 0; width: 100%; top: 600px;
    text-align: center; color: var(--ink-grey);
    font: 400 35px/1 "Poiret One", sans-serif;
  }
  .style {
    position: absolute; left: 0; width: 100%; top: 650px;
    text-align: center; color: var(--ink-grey);
    font: 400 29px/1 "Tinos", serif; letter-spacing: 0.5px;
  }
  .footer-ornament {
    position: absolute; left: 312px; top: 704px;
    width: 120px; height: 30px;
    background: radial-gradient(ellipse at center, var(--gold) 0%, var(--gold-soft) 45%, rgba(20,20,20,0) 75%);
  }
</style>
</head>
<body>
<main class="canvas">
  <section class="label">
    <svg class="label-shape" width="744" height="792" viewBox="0 0 744 792">
      <defs>
        <radialGradient id="label-fill" cx="50%" cy="45%" r="65%">
          <stop offset="0" stop-color="#1c1c1c"/>
          <stop offset="1" stop-color="#0c0c0c"/>
        </radialGradient>
      </defs>
      <path d="M56 0 H688 A56 56 0 0 0 744 56 V736 A56 56 0 0 0 688 792 H56 A56 56 0 0 0 0 736 V56 A56 56 0 0 0 56 0 Z"
            fill="url(#label-fill)" stroke="var(--label-edge)" stroke-width="2"/>
      <path d="M84 30 H660 A54 54 0 0 0 714 84 V708 A54 54 0 0 0 660 762 H84 A54 54 0 0 0 30 708 V84 A54 54 0 0 0 84 30 Z"
            fill="none" stroke="var(--gold)" stroke-width="3.5" stroke-dasharray="20 14" stroke-linecap="round"/>
      <line x1="120" y1="308" x2="336" y2="308" stroke="var(--gold)" stroke-width="3"/>
      <line x1="408" y1="308" x2="678" y2="308" stroke="var(--gold)" stroke-width="3"/>
      <line x1="252" y1="719" x2="312" y2="719" stroke="var(--gold)" stroke-width="2"/>
      <line x1="432" y1="719" x2="552" y2="719" stroke="var(--gold)" stroke-width="2"/>
    </svg>

    <div class="crest" role="img" aria-label="Gold-edged heraldic shield with Italian tricolour and laurel sprigs"></div>
    <p class="product-type">Prosecco</p>
    <div class="divider-ornament" role="img" aria-label="Gold scroll ornament at centre of divider line"></div>
    <h1 class="wine-name">Vuro</h1>
    <p class="region">Veneto</p>
    <p class="appellation">Indicazione Geografica Tipica</p>
    <p class="style">FRIZZANTE</p>
    <div class="footer-ornament" role="img" aria-label="Gold calligraphic flourish"></div>
  </section>
</main>
</body>
</html>
```